Fun Location App for users to earn rewards and vouchers everywhere they go

Jorvix is a social app where users can collect rewards when they travel + complete quests at different location to get rewards.

We would like a design of an app that has these features/function
1) Login/Signup Page
2) HomePage - A Map with your current location
- Show the location/stores aroudn
- Have a bag tab to press and get rewards
3) Quests Tab = show all the available tasks
4) Exchange Tab = all the items available for exchange vouchers and can click to know more
5) Wallet Tab = user profile + vouchers in their wallet
6) Partners Tab = Showcase all the partners and can click to know more
7) Claim functions

We have attached a visual example. Do feel free to change what is best fit too. We do need to exact measurements as well to create the app

Target Market(s)

Fun, people who like rewards and interact with friends

Font styles to use
Sans Serif

Colors
f78f20
fbed22
fbee3e

Requirements
Must have
• Yellow, fun interactive feeling.
Nice to have
• Pop up when click on things
Should not have
• nil

```html
<!DOCTYPE html>
<html lang="en">
<head>
<meta charset="utf-8">
<title>Jorvix app screens</title>
<link rel="stylesheet" href="https://fonts.googleapis.com/css2?family=Quicksand:wght@500;700&display=swap">
<style>
:root{
  --stage:#fbbd0c;
  --orange:#f7941d;
  --amber:#fdc520;
  --yellow:#fbc916;
  --ink:#4a4f63;
  --logo-grey:#58595b;
  --map:#3f4560;
  --map-dim:#363c55;
  --white:#ffffff;
  --field-text:#555a6b;
  --grey-pop:#5b6490;
  --edge:rgba(74,79,99,.18);
}
*{box-sizing:border-box;margin:0;padding:0}
html,body{width:1200px;height:2594px;overflow:hidden}
body{background:var(--stage);font-family:"Quicksand",sans-serif;position:relative;color:var(--ink)}

.brand{position:absolute;display:flex;align-items:center;gap:10px;font-weight:700;letter-spacing:-1px;white-space:nowrap}
.brand .dot{border-radius:50%;flex:none}
.brand-corner{left:905px;top:140px;font-size:58px;color:var(--logo-grey)}
.brand-corner .dot{width:22px;height:22px;background:var(--yellow)}

.screen{position:absolute;overflow:hidden;border-radius:30px;box-shadow:0 0 0 1px var(--edge)}
.screen.orange{background:linear-gradient(180deg,var(--orange) 0%,var(--amber) 100%)}

.splash{left:398px;top:88px;width:434px;height:942px;border-radius:46px}
.ring{position:absolute;border-radius:50%;left:50%;top:473px;transform:translate(-50%,-50%)}
.ring.r1{width:352px;height:352px;background:rgba(255,255,255,.12)}
.ring.r2{width:292px;height:292px;background:rgba(255,255,255,.22)}
.ring.r3{width:236px;height:236px;background:rgba(255,255,255,.55)}
.ring.r4{width:180px;height:180px;background:var(--white)}
.splash .brand{left:50%;top:473px;transform:translate(-50%,-50%);font-size:34px;color:var(--logo-grey);gap:6px}
.splash .brand .dot{width:12px;height:12px;background:var(--yellow)}

.small{width:257px;height:560px}
.login{left:75px;top:1162px}
.signup{left:462px;top:1162px}

.welcome{position:absolute;left:90px;top:201px;font-size:6px;font-weight:700;color:var(--white)}
.screen .brand.light{color:var(--white);font-size:26px;gap:5px;left:50%;transform:translateX(-50%)}
.brand.light .dot{width:9px;height:9px;border:2px solid var(--white)}

.field{position:absolute;left:16px;width:224px;height:27px;background:var(--white);font-size:6px;color:var(--field-text);display:flex;align-items:center;padding:0 11px;white-space:nowrap}
.field .value{margin-left:10px;color:var(--ink)}
.otp-dots{margin-left:6px;font-size:9px;letter-spacing:1px;color:var(--ink)}
.get-code{margin-left:auto;background:var(--yellow);color:var(--white);font-size:5px;padding:3px 12px}
.consent{position:absolute;left:40px;right:40px;top:336px;font-size:4px;text-align:center;color:var(--ink);line-height:1.7}
.btn{position:absolute;height:20px;background:var(--ink);color:var(--white);font-size:5px;display:flex;align-items:center;justify-content:center;gap:14px;border-radius:2px}
.powered{position:absolute;left:0;right:0;top:513px;text-align:center;color:var(--white);font-size:7px;font-weight:700;line-height:1.8}
.subhead{position:absolute;left:0;right:0;top:155px;text-align:center;font-size:6px;font-weight:700;color:var(--white)}
.select-caret{margin-left:auto;width:0;height:0;border-left:3px solid transparent;border-right:3px solid transparent;border-top:4px solid #888}

.map-screen{background:var(--map)}
.map-screen.s1{left:849px;top:1162px}
.map-screen.s2{left:271px;top:1857px}
.map-screen.s3{left:664px;top:1857px}
.map-fill{position:absolute;inset:0;background:radial-gradient(circle at 45% 55%,#4a5170 0%,var(--map) 45%,var(--map-dim) 100%)}
.clock{position:absolute;left:21px;top:6px;font-size:8px;color:var(--white)}
.status{position:absolute;right:16px;top:8px;width:14px;height:6px;background:var(--white);border-radius:1px}
.gear{position:absolute;left:218px;top:22px;width:20px;height:20px}
.pin{position:absolute;width:20px;height:26px;transform:translate(-50%,-100%)}
.radar{position:absolute;width:70px;height:70px;border-radius:50%;background:rgba(251,189,12,.35);transform:translate(-50%,-50%)}
.radar::after{content:"";position:absolute;left:50%;top:50%;width:14px;height:14px;border-radius:50%;background:var(--yellow);transform:translate(-50%,-50%);box-shadow:0 0 0 8px rgba(251,189,12,.45)}
.landmark{position:absolute;width:43px;height:40px;background:var(--white);border:2px solid var(--yellow);font-size:4.5px;text-align:center;color:var(--ink);padding-top:25px;white-space:nowrap}
.landmark::before{content:"";position:absolute;left:50%;top:5px;width:16px;height:16px;border-radius:50%;transform:translateX(-50%);background:#cfd8e6}
.landmark::after{content:"";position:absolute;left:50%;bottom:-7px;transform:translateX(-50%);border-left:5px solid transparent;border-right:5px solid transparent;border-top:6px solid var(--yellow)}
.bag{position:absolute;left:82px;top:445px;width:92px;height:56px;background:var(--yellow);padding:3px 6px;text-align:center;font-size:4.5px;color:var(--ink);line-height:2.6}
.bag.empty{background:var(--grey-pop);color:#b7bdd8}
.bag .open{background:var(--ink);color:var(--white);font-weight:700;height:18px;line-height:18px;margin-bottom:2px}
.ads{position:absolute;left:17px;top:59px;width:224px;height:27px;background:var(--white);border:1px solid #ccc;font-size:9px;display:flex;align-items:center;justify-content:center;color:var(--ink)}
.tabbar{position:absolute;left:0;right:0;bottom:0;height:46px;background:var(--white);display:flex;align-items:center;justify-content:space-around;padding:0 10px}
.tab{width:22px;height:18px;border:1.5px solid #b9bcc6;border-radius:3px}
.tab.narrow{width:14px}
.tab.round{border-radius:50%;width:20px;height:20px}
.tab.home{border-style:dashed}
.tab-main{width:40px;height:40px;border-radius:50%;background:var(--yellow);display:flex;align-items:center;justify-content:center;margin-top:-4px;box-shadow:0 0 0 2px #f7a81d}
</style>
</head>
<body>
<svg width="0" height="0" style="position:absolute">
  <symbol id="pin" viewBox="0 0 20 26"><path d="M10 1a9 9 0 0 1 9 9c0 6-9 15-9 15S1 16 1 10a9 9 0 0 1 9-9z" fill="#fbc916" stroke="#f29b12" stroke-width="1"/><circle cx="10" cy="10" r="4" fill="#3f4560"/></symbol>
  <symbol id="gear" viewBox="0 0 20 20"><circle cx="10" cy="10" r="7" fill="none" stroke="#fff" stroke-width="4" stroke-dasharray="3 2.5"/><circle cx="10" cy="10" r="5" fill="none" stroke="#fff" stroke-width="2.5"/></symbol>
</svg>

<div class="brand brand-corner"><span class="dot"></span>jorvix</div>

<section class="screen orange splash">
  <div class="ring r1"></div><div class="ring r2"></div><div class="ring r3"></div><div class="ring r4"></div>
  <div class="brand"><span class="dot"></span>jorvix</div>
</section>

<section class="screen orange small login">
  <p class="welcome">WELCOME TO</p>
  <div class="brand light" style="top:204px"><span class="dot"></span>jorvix</div>
  <div class="field" style="top:265px">Mobile Number : <span class="value">+999 9999 999</span></div>
  <div class="field" style="top:301px">OTP : <span class="otp-dots">●●●●●●</span><span class="get-code">GET CODE</span></div>
  <p class="consent">By login / signup , you have agreed to Term of Use and Privacy Policy on Jorvix Pte Ltd.</p>
  <div class="btn" style="left:44px;width:166px;top:361px"><span>LOGIN</span><span>|</span><span>SIGNUP</span></div>
  <p class="powered">Powered By<br>Harmonic Ledger</p>
</section>

<section class="screen orange small signup">
  <div class="brand light" style="top:118px"><span class="dot"></span>jorvix</div>
  <p class="subhead">NEW USER SIGNUP</p>
  <div class="field" style="top:180px">First Name *</div>
  <div class="field" style="top:216px">Last Name *</div>
  <div class="field" style="top:251px">Username *</div>
  <div class="field" style="top:287px">Date of Birth *</div>
  <div class="field" style="top:322px">Email*</div>
  <div class="field" style="top:358px">Referral Code / Account Code*</div>
  <div class="field" style="top:394px">Gender *<span class="select-caret"></span></div>
  <div class="btn" style="left:45px;width:166px;top:445px">NEXT</div>
  <p class="powered">Powered By<br>Harmonic Ledger</p>
</section>

<section class="screen small map-screen s1">
  <div class="map-fill" role="img" aria-label="Dark street map of a city square around the user's location"></div>
  <span class="clock">22:47</span><span class="status"></span>
  <svg class="gear"><use href="#gear"/></svg>
  <svg class="pin" style="left:117px;top:80px"><use href="#pin"/></svg>
  <svg class="pin" style="left:54px;top:147px"><use href="#pin"/></svg>
  <svg class="pin" style="left:226px;top:195px"><use href="#pin"/></svg>
  <svg class="pin" style="left:231px;top:334px"><use href="#pin"/></svg>
  <svg class="pin" style="left:30px;top:406px"><use href="#pin"/></svg>
  <div class="landmark" style="left:113px;top:146px">riverside wheel</div>
  <div class="radar" style="left:117px;top:294px"></div>
  <div class="bag"><div class="open">OPEN YOUR BAG</div>5000 x jorpoints<br>5x voucher</div>
  <nav class="tabbar"><span class="tab home"></span><span class="tab"></span><span class="tab-main"><svg width="20" height="26"><use href="#pin"/></svg></span><span class="tab narrow"></span><span class="tab round"></span></nav>
</section>

<section class="screen small map-screen s2">
  <div class="map-fill" role="img" aria-label="Dark street map of a city square around the user's location"></div>
  <span class="clock">22:47</span><span class="status"></span>
  <svg class="gear"><use href="#gear"/></svg>
  <svg class="pin" style="left:116px;top:78px"><use href="#pin"/></svg>
  <svg class="pin" style="left:54px;top:145px"><use href="#pin"/></svg>
  <svg class="pin" style="left:135px;top:195px"><use href="#pin"/></svg>
  <svg class="pin" style="left:226px;top:195px"><use href="#pin"/></svg>
  <svg class="pin" style="left:231px;top:334px"><use href="#pin"/></svg>
  <svg class="pin" style="left:29px;top:406px"><use href="#pin"/></svg>
  <div class="radar" style="left:118px;top:294px"></div>
  <div class="bag empty"><div class="open">OPEN YOUR BAG</div>0 x jorpoints<br>0 x voucher</div>
  <nav class="tabbar"><span class="tab home"></span><span class="tab"></span><span class="tab-main"><svg width="20" height="26"><use href="#pin"/></svg></span><span class="tab narrow"></span><span class="tab round"></span></nav>
</section>

<section class="screen small map-screen s3">
  <div class="map-fill" role="img" aria-label="Dark street map of a city square around the user's location"></div>
  <span class="clock">22:47</span><span class="status"></span>
  <svg class="gear"><use href="#gear"/></svg>
  <div class="ads">ADS / MESSAGE</div>
  <svg class="pin" style="left:54px;top:145px"><use href="#pin"/></svg>
  <svg class="pin" style="left:226px;top:195px"><use href="#pin"/></svg>
  <svg class="pin" style="left:231px;top:334px"><use href="#pin"/></svg>
  <svg class="pin" style="left:29px;top:406px"><use href="#pin"/></svg>
  <div class="landmark" style="left:113px;top:146px">riverside wheel</div>
  <div class="radar" style="left:118px;top:294px"></div>
  <div class="bag"><div class="open">OPEN YOUR BAG</div>5000 x jorpoints<br>5x voucher</div>
  <nav class="tabbar"><span class="tab home"></span><span class="tab"></span><span class="tab-main"><svg width="20" height="26"><use href="#pin"/></svg></span><span class="tab narrow"></span><span class="tab round"></span></nav>
</section>
</body>
</html>
```